HIGH-END ANTI AGING START-UP NEEDS DOCUMENT/LETTERHEAD DESIGN!!!!

We are a high end anti-aging and health start-up catering to clients in Stamford and NYC. We just did a logo redesign and are now looking for a letter head design that we can use IN GOOGLE DOCS for marrowfieldcaregroup.example clients. We are REALLY EXCITED to see what you can show us!!!!!!!! We need something sophisticated and MODERN! Thanks so much!

Target Market(s)

High end, boutique medical clients. Our clientele is fairly high profile and we need a sleek, sophisticated letter head to put on all of our marketing materials and medical forms as well.

Industry/Entity Type

Medical

Font styles to use
Serif
Sans Serif

Colors
0255a3
ffffff
00a990
1b1b1b
919191

Requirements
Must have
• Must have the logo and "Marrowfield Care Group" written somewhere. Must have our URL www.marrowfieldcaregroup.example.
Nice to have
• office phone number (555) 374-9102
Should not have
• Colors outside of our logo colors + grey + black

```html
<!DOCTYPE html>
<html lang="en">
<head>
<meta charset="utf-8">
<title>Marrowfield Care Group Letterhead</title>
<link href="https://fonts.googleapis.com/css2?family=Open+Sans:wght@400;600&display=swap" rel="stylesheet">
<style>
  :root {
    --backdrop: #eeeeee;
    --paper: #ffffff;
    --brand-blue: #4a80e6;
    --brand-green: #009444;
    --watermark-mint: #e4f3eb;
    --ink: #1b1b1b;
    --muted: #919191;
  }
  * { margin: 0; padding: 0; box-sizing: border-box; }
  html, body {
    width: 1200px; height: 1200px; overflow: hidden;
    background: var(--backdrop);
    font-family: "Open Sans", Arial, sans-serif;
  }
  .letterhead {
    position: absolute; left: 220px; top: 30px;
    width: 760px; height: 1140px;
    background: var(--paper);
    overflow: hidden;
  }
  .letterhead__art { position: absolute; inset: 0; }
  .brand {
    position: absolute; right: 60px; top: 40px;
    display: flex; flex-direction: column; align-items: flex-end; gap: 14px;
  }
  .brand__dot {
    width: 72px; height: 72px; border-radius: 50%;
    background: var(--brand-green);
    margin-right: 38px;
  }
  .brand__name {
    font-weight: 600; font-size: 17px; line-height: 1.15;
    letter-spacing: 2px; text-transform: uppercase;
    color: var(--brand-blue); text-align: center;
  }
  .contact {
    position: absolute; left: 52px; top: 1071px;
    list-style: none; font-size: 11.5px; color: var(--ink);
  }
  .contact__item { display: flex; align-items: center; gap: 10px; height: 18px; }
  .contact__icon { width: 10px; height: 10px; }
</style>
</head>
<body>
  <main class="letterhead">
    <svg class="letterhead__art" width="760" height="1140" viewBox="0 0 760 1140" aria-hidden="true">
      <polygon class="corner corner--top" points="0,0 89,0 0,140" fill="var(--brand-blue)"/>
      <circle class="watermark" cx="404" cy="598" r="341" fill="var(--watermark-mint)"/>
      <polygon class="corner corner--bottom" points="760,1009 760,1140 680,1140" fill="var(--brand-green)"/>
    </svg>

    <header class="brand">
      <span class="brand__dot"></span>
      <div class="brand__name">Marrowfield<br>Care Group</div>
    </header>

    <ul class="contact">
      <li class="contact__item">
        <svg class="contact__icon" viewBox="0 0 10 10" aria-hidden="true">
          <path d="M3 0.5 L4.5 2.5 L3.5 3.5 Q4.5 6 6.5 6.8 L7.5 5.8 L9.5 7.3 L8.5 9 Q3 9 1 2 Z" fill="var(--brand-blue)"/>
        </svg>
        <span>(555) 374-9102</span>
      </li>
      <li class="contact__item">
        <svg class="contact__icon" viewBox="0 0 10 10" aria-hidden="true">
          <g fill="none" stroke="var(--brand-blue)" stroke-width="0.8">
            <circle cx="5" cy="5" r="4.3"/>
            <ellipse cx="5" cy="5" rx="1.9" ry="4.3"/>
            <line x1="0.7" y1="5" x2="9.3" y2="5"/>
          </g>
        </svg>
        <span>www.marrowfieldcaregroup.example</span>
      </li>
    </ul>
  </main>
</body>
</html>
```